KORBALT

The business want a professional looking business card. We have a scetch we will add but want the extra upgrade, and would like more suggestions for variations of our business cards.

```html
<!DOCTYPE html>
<html lang="en">
<head>
<meta charset="utf-8">
<title>KORBALT Business Card</title>
<link rel="stylesheet" href="https://fonts.googleapis.com/css2?family=Montserrat:wght@400;500;700&display=swap">
<style>
  :root {
    --backdrop: #121212;
    --card: #1d1d1d;
    --card-edge: #262626;
    --gold: #caa34c;
    --gold-soft: #a8843a;
    --ink-light: #f1f1f1;
    --pattern-dark: #191919;
    --pattern-light: #4a4a4a;
  }
  html, body {
    margin: 0;
    padding: 0;
    width: 1200px;
    height: 1059px;
    overflow: hidden;
    background: var(--backdrop);
    font-family: "Montserrat", Arial, sans-serif;
  }
  .canvas {
    position: relative;
    width: 1200px;
    height: 1059px;
  }
  .card {
    position: absolute;
    background: var(--card);
    border-radius: 18px;
    overflow: hidden;
    box-shadow: 0 10px 24px rgba(0,0,0,0.55);
  }
  .card--front {
    left: 257px;
    top: 89px;
    width: 687px;
    height: 390px;
  }
  .card--back {
    left: 254px;
    top: 546px;
    width: 693px;
    height: 394px;
  }
  .brand {
    position: absolute;
    display: flex;
    flex-direction: column;
    align-items: center;
    transform: translateX(-50%);
  }
  .brand__dot {
    width: 58px;
    height: 58px;
    border-radius: 50%;
    background: var(--gold);
    margin-bottom: 22px;
  }
  .brand__name {
    font-family: "Montserrat", Arial, sans-serif;
    font-weight: 500;
    color: var(--gold);
    letter-spacing: 0.22em;
    margin-right: -0.22em;
    line-height: 1;
  }
  .card--front .brand {
    left: 343px;
    top: 50px;
  }
  .card--front .brand__dot {
    width: 96px;
    height: 96px;
    margin-top: 8px;
    margin-bottom: 40px;
  }
  .card--front .brand__name {
    font-size: 27px;
  }
  .identity {
    position: absolute;
    right: 365px;
    top: 270px;
    text-align: right;
  }
  .identity__name {
    margin: 0;
    font-size: 22px;
    font-weight: 700;
    color: var(--gold);
    line-height: 1.15;
  }
  .identity__role {
    margin: 2px 0 0;
    font-size: 18px;
    font-weight: 400;
    color: var(--ink-light);
  }
  .divider {
    position: absolute;
    left: 346px;
    top: 258px;
    width: 1px;
    height: 75px;
    background: var(--gold-soft);
  }
  .contacts {
    position: absolute;
    left: 368px;
    top: 252px;
    margin: 0;
    padding: 0;
    list-style: none;
  }
  .contacts__item {
    display: flex;
    align-items: center;
    height: 31.5px;
    font-size: 18px;
    color: var(--ink-light);
    letter-spacing: 0.02em;
  }
  .contacts__icon {
    width: 15px;
    height: 15px;
    margin-right: 10px;
    flex: none;
  }
  .pattern {
    position: absolute;
    inset: 0;
    background: linear-gradient(100deg, var(--pattern-dark) 0%, var(--pattern-dark) 35%, var(--pattern-light) 100%);
    opacity: 0.85;
  }
  .card--back .brand {
    left: 546px;
    top: 165px;
  }
  .card--back .brand__name {
    font-size: 21px;
  }
</style>
</head>
<body>
<div class="canvas">

  <section class="card card--front">
    <div class="brand">
      <div class="brand__dot"></div>
      <div class="brand__name">KORBALT</div>
    </div>

    <div class="identity">
      <p class="identity__name">Aksel Rune Vindholm</p>
      <p class="identity__role">CEO &amp; Founder</p>
    </div>

    <div class="divider"></div>

    <ul class="contacts">
      <li class="contacts__item">
        <svg class="contacts__icon" viewBox="0 0 16 16" aria-hidden="true">
          <path fill="var(--gold)" d="M3.2 1.5l2.3 2.4-1.2 1.8c.9 2 2.3 3.4 4.2 4.3l1.8-1.2 2.4 2.3-1.3 2.2C6.9 13.2 2.6 9 1 4.2z"/>
        </svg>
        004791234560
      </li>
      <li class="contacts__item">
        <svg class="contacts__icon" viewBox="0 0 16 16" aria-hidden="true">
          <path fill="var(--gold)" d="M1 5.5L8 1l7 4.5V15H1z"/>
          <path fill="none" stroke="var(--card)" stroke-width="1.2" d="M1.5 6l6.5 4.5L14.5 6"/>
        </svg>
        hello@korbalt.llc
      </li>
      <li class="contacts__item">
        <svg class="contacts__icon" viewBox="0 0 16 16" aria-hidden="true">
          <circle cx="8" cy="8" r="7" fill="var(--gold)"/>
          <path fill="none" stroke="var(--card)" stroke-width="1.1" d="M1 8h14M8 1c-2.5 2.5-2.5 11.5 0 14M8 1c2.5 2.5 2.5 11.5 0 14"/>
        </svg>
        www.korbalt.llc
      </li>
    </ul>
  </section>

  <section class="card card--back">
    <div class="pattern" role="img" aria-label="Repeating decorative pattern fading from black to silver across the card"></div>
    <div class="brand">
      <div class="brand__dot"></div>
      <div class="brand__name">KORBALT</div>
    </div>
  </section>

</div>
</body>
</html>
```